Law Office Business Card

We need a business card design to include the following information:
Name of Firm: Halvern Law Group, P.A.
Address: 2417 Osprey Ln, Ste 208, West Palm Beach, FL 33512
Phone: 561-390-7752
Fax: 561-390-7789
Website: http://www.bhalvernlaw.example

We Need a place for the Person's name and email address. Please start with the following:
Lorna K. Tibbett, Esq.
lorna@bhalvernlaw.example

Industry/Entity Type

Business

```html
<!DOCTYPE html>
<html lang="en">
<head>
<meta charset="utf-8">
<title>Halvern Law Group – Business Cards</title>
<link rel="stylesheet" href="https://fonts.googleapis.com/css2?family=Crimson+Text:wght@400;600&display=swap">
<style>
  :root {
    --bg: #ece6dc;
    --navy: #125577;
    --navy-deep: #0f4a69;
    --silver-light: #f4f4f5;
    --silver-mid: #d9dadc;
    --silver-dark: #b9bbbe;
    --white: #ffffff;
    --sky: #8aa6bd;
  }
  * { margin: 0; padding: 0; box-sizing: border-box; }
  html, body { width: 1051px; height: 1200px; overflow: hidden; }
  body {
    background: var(--bg);
    position: relative;
    font-family: "Crimson Text", Georgia, serif;
  }
  .card {
    position: absolute;
    width: 788px;
    height: 457px;
    overflow: hidden;
    box-shadow: 0 2px 6px rgba(0,0,0,.18);
  }
  .card--front { left: 126px; top: 102px; }
  .card--back  { left: 131px; top: 620px; }

  .brand-panel {
    position: absolute; left: 0; top: 0; bottom: 0; width: 288px;
    background: linear-gradient(90deg, var(--silver-dark) 0%, var(--silver-light) 45%, var(--silver-mid) 100%);
  }
  .separator {
    position: absolute; left: 288px; top: 0; bottom: 0; width: 18px;
    background: var(--navy);
  }
  .separator::after {
    content: ""; position: absolute; left: 6px; top: 0; bottom: 0; width: 6px;
    background: linear-gradient(180deg, #8c9298, #f2f3f4 50%, #8c9298);
  }
  .info-panel {
    position: absolute; left: 306px; top: 0; right: 0; bottom: 0;
    background: var(--navy);
  }

  .brand-name {
    position: absolute; left: 0; width: 288px; top: 100px;
    text-align: center; color: var(--navy);
    font-weight: 400; font-size: 38px; line-height: 1.05; letter-spacing: 1px;
  }
  .firm-line, .web-line {
    position: absolute; left: 0; width: 288px; text-align: center;
    color: var(--navy); font-size: 22px;
  }
  .firm-line { top: 270px; }
  .web-line { top: 330px; font-size: 23px; letter-spacing: .3px; }

  .photo-skyline-front {
    position: absolute; left: 0; top: 0; right: 0; height: 175px;
    background: linear-gradient(180deg, #5e86a3 0%, #3e6f8f 60%, var(--navy) 100%);
  }
  .photo-skyline-back {
    position: absolute; left: 0; top: 292px; width: 288px; height: 135px;
    background: linear-gradient(180deg, rgba(230,233,236,0) 0%, #c9d5df 30%, #a9b3bb 65%, rgba(220,223,226,.4) 100%);
  }

  .contact { position: absolute; left: 50px; color: var(--white); }
  .card--front .contact { top: 180px; }
  .card--back .contact { top: 130px; }
  .person-name { font-weight: 600; font-size: 26px; margin-bottom: 14px; }
  .contact-row {
    display: flex; align-items: flex-start; gap: 8px;
    font-size: 24px; line-height: 36px;
  }
  .contact-row svg { flex: none; margin-top: 9px; width: 22px; height: 20px; }
  .contact-row .address { line-height: 36px; }
  .firm-heading {
    position: absolute; right: 24px; top: 40px;
    color: var(--white); font-weight: 600; font-size: 25px;
  }
  .web-row { margin-top: 10px; }
</style>
</head>
<body>

<section class="card card--front">
  <div class="brand-panel">
    <div class="brand-name">HALVERN<br>LAW<br>GROUP</div>
    <div class="firm-line">Halvern Law Group, P.A.</div>
    <div class="web-line">www.bhalvernlaw.example</div>
  </div>
  <div class="separator"></div>
  <div class="info-panel">
    <div class="photo-skyline-front" role="img" aria-label="City waterfront skyline photograph, tinted blue"></div>
    <div class="contact">
      <div class="person-name">Lorna K. Tibbett, Esq.</div>
      <div class="contact-row">
        <svg viewBox="0 0 22 16"><rect x="1" y="1" width="20" height="14" fill="none" stroke="#fff" stroke-width="2"/><path d="M1 1 L11 9 L21 1" fill="none" stroke="#fff" stroke-width="2"/></svg>
        <span>lorna@bhalvernlaw.example</span>
      </div>
      <div class="contact-row">
        <svg viewBox="0 0 20 20"><path d="M4 1 L8 5 L6 8 C7 11 9 13 12 14 L15 12 L19 16 L16 19 C8 18 2 12 1 4 Z" fill="#fff"/></svg>
        <span>561-390-7752</span>
      </div>
      <div class="contact-row">
        <svg viewBox="0 0 22 20"><rect x="5" y="1" width="12" height="6" fill="#fff"/><rect x="1" y="8" width="20" height="11" rx="1" fill="#fff"/><rect x="5" y="12" width="12" height="2" fill="#125577"/></svg>
        <span>561-390-7789</span>
      </div>
      <div class="contact-row">
        <svg viewBox="0 0 16 24" style="height:26px"><path d="M8 1 C4 1 1 4 1 8 C1 13 8 23 8 23 C8 23 15 13 15 8 C15 4 12 1 8 1 Z" fill="#fff"/><circle cx="8" cy="8" r="3" fill="#125577"/></svg>
        <span class="address">2417 Osprey Ln, Ste 208,<br>West Palm Beach, FL 33512</span>
      </div>
    </div>
  </div>
</section>

<section class="card card--back">
  <div class="brand-panel">
    <div class="brand-name">HALVERN<br>LAW<br>GROUP</div>
    <div class="photo-skyline-back" role="img" aria-label="City waterfront skyline photograph fading into silver"></div>
  </div>
  <div class="separator"></div>
  <div class="info-panel">
    <div class="firm-heading">Halvern Law Group, P.A.</div>
    <div class="contact">
      <div class="person-name">Lorna K. Tibbett, Esq.</div>
      <div class="contact-row">
        <svg viewBox="0 0 22 16"><rect x="1" y="1" width="20" height="14" fill="none" stroke="#fff" stroke-width="2"/><path d="M1 1 L11 9 L21 1" fill="none" stroke="#fff" stroke-width="2"/></svg>
        <span>lorna@bhalvernlaw.example</span>
      </div>
      <div class="contact-row">
        <svg viewBox="0 0 20 20"><path d="M4 1 L8 5 L6 8 C7 11 9 13 12 14 L15 12 L19 16 L16 19 C8 18 2 12 1 4 Z" fill="#fff"/></svg>
        <span>561-390-7752</span>
      </div>
      <div class="contact-row">
        <svg viewBox="0 0 22 20"><rect x="5" y="1" width="12" height="6" fill="#fff"/><rect x="1" y="8" width="20" height="11" rx="1" fill="#fff"/><rect x="5" y="12" width="12" height="2" fill="#125577"/></svg>
        <span>561-390-7789</span>
      </div>
      <div class="contact-row">
        <svg viewBox="0 0 16 24" style="height:26px"><path d="M8 1 C4 1 1 4 1 8 C1 13 8 23 8 23 C8 23 15 13 15 8 C15 4 12 1 8 1 Z" fill="#fff"/><circle cx="8" cy="8" r="3" fill="#125577"/></svg>
        <span class="address">2417 Osprey Ln, Ste 208,<br>West Palm Beach, FL 33512</span>
      </div>
      <div class="contact-row web-row">
        <svg viewBox="0 0 22 22"><circle cx="11" cy="11" r="9" fill="none" stroke="#fff" stroke-width="1.8"/><ellipse cx="11" cy="11" rx="4" ry="9" fill="none" stroke="#fff" stroke-width="1.5"/><path d="M2 11 H20 M4 6 H18 M4 16 H18" stroke="#fff" stroke-width="1.3"/></svg>
        <span>www.bhalvernlaw.example</span>
      </div>
    </div>
  </div>
</section>

</body>
</html>
```